meditation/yoga retreat eco village ashram commune website

There is a group of 20-30 people living in the jungle of mexico. We all came together from all walks of life to help built a paradise on earth. This is a meditation ashram resort that is built by a living enlightenment master, a modern day buddha master Swami Devakar Lunel. It's his vision and his love that he wants to share to the world.

The eco village project is on a 19 hectares forest land with a cenote (natural pond) as the heart centre surrounded by beautiful tropical gardens. This unique village is conceived in a mystical mayan circle as an oasis for creative arts crafts music and dance, mayan wisdom, eastern ayurveda, yoga, vipassana, meditation and silent retreat for the science of inner transformation this eco development will offer residents and visitors the experience of nature, silence, tranquility, meditativeness and a compassionate space for growth and flowering of human consciousness.

we are creating an inner science mystery school where we will offer ancient mayan traditions, buddhist vipassana, tibetan teachings, yoga, patanjali yoga, pranayama, we will also offer meditations and therapies like mystic rose, born again, no mind, painting group, breath, prana healing, primal, work as meditation all therapies and meditations will be offered for free we accept donations out of gratitude

The NEW DOMAIN for this website will be - www.LUNELTIKAL.example

This is our old website - http://luneldevakar.example/o/tikal/
it is outdated and we haven't done anything to it in the past 5 years. Now that we are about to open to the world, we want a fresh new look that will captivate our audience. Please take a moment to browse our website to get an idea of who we are.

Also please check out our facebook page, you will see all our past events, upcoming events with pics and videos.
www.facebook.example/luneltikal
www.instagram.example/luneltikal

We have 3 festivals coming up, they are as follows.
Yoga festival - https://www.facebook.example/events/4402918837165530/
Art festival - https://www.facebook.example/events/4409357162093341/
Thai massage - https://www.facebook.example/events/8835461290057213/

Do not use any of the pictures from the old website, it is outdated, most are just drawings and sketches. I have zipped up some great pictures for you to use, ...also feel free to use anything from facebook/instagram as well.

For menu, also we will have sub-categories menu for each as well.

HOME
NEWS
THE PROJECT
EVENTS
VIDEOS
PHOTOS
TICKETS
RESIDENTIAL
DONATE
CONTACT

Things to include for main page.
*Upcoming Events
*Previous Pics/Videos of Past Events (grab them from our facebook page)
*Show some great construction building, reed pavilion, fern pavilion, welcome center, etc..
*Maybe a section where the master can say a message.
*Mediation/Yoga section
*Residential Booking
*Facebook page, *twitter feed, instagram, youtube channel

Target Market(s)

meditation, yoga, art, dance festivals

Industry/Entity Type

Group

Number of Pages Required

1 page

Requirements
Must have
• we are looking for something classy, elegant, yet simple...stay away from traditional, give it a really cool modern touch.

```html
<!DOCTYPE html>
<html lang="en">
<head>
<meta charset="utf-8">
<title>Lunel Tikal — Meditation &amp; Yoga Eco Village</title>
<link href="https://fonts.googleapis.com/css2?family=Open+Sans:wght@400;600;700;800&family=Montserrat:wght@400;600;700&display=swap" rel="stylesheet">
<style>
:root{
  --red:#d0111b;
  --ink:#222;
  --text:#555;
  --muted:#888;
  --light:#f4f4f4;
  --line:#ddd;
  --dark:#1c1c1c;
  --white:#fff;
}
*{box-sizing:border-box;margin:0;padding:0}
html,body{width:1200px;height:4476px;overflow:hidden}
body{font-family:"Open Sans",Arial,sans-serif;color:var(--text);background:var(--white);position:relative}
.section{position:absolute;left:0;width:1200px}
.section-title{font-family:"Montserrat",Arial,sans-serif;font-weight:400;font-size:30px;letter-spacing:2px;text-align:center;color:var(--ink);text-transform:uppercase}
.section-title em{font-style:normal;color:var(--red);font-weight:700}
.title-mark{display:block;width:22px;height:22px;background:var(--ink);margin:14px auto 0;position:relative}
.title-mark::after{content:"";position:absolute;inset:6px;border:2px solid var(--white)}
.btn{display:inline-block;background:var(--red);color:var(--white);font-weight:700;font-size:15px;letter-spacing:1px;text-transform:uppercase;text-align:center;padding:14px 0;border-radius:4px}

/* hero */
.hero{top:0;height:870px;background:var(--dark)}
.hero-photo{position:absolute;inset:0 0 190px 0;background:linear-gradient(180deg,#2b2014 0%,#5a3f22 35%,#7b5a35 55%,#3e4a2a 80%,#2a2a1c 100%)}
.brand{position:absolute;left:40px;top:44px;display:flex;align-items:center;gap:10px}
.brand-square{width:20px;height:20px;background:var(--white)}
.brand-name{font-weight:700;font-size:22px;color:var(--white);letter-spacing:2px;white-space:nowrap}
.social-top{position:absolute;right:40px;top:26px;display:flex;gap:10px}
.social-top span{width:20px;height:20px;border-radius:50%;background:rgba(255,255,255,.85)}
.main-nav{position:absolute;left:200px;right:40px;top:100px;height:46px;background:rgba(30,30,30,.85);display:flex;align-items:center;padding:0 10px;gap:4px}
.main-nav a{color:#ddd;font-size:14px;text-decoration:none;padding:12px 18px}
.main-nav a.active{background:var(--red);color:var(--white)}
.slider-dots{position:absolute;left:0;right:0;top:632px;display:flex;justify-content:center;gap:10px}
.slider-dots span{width:12px;height:12px;border-radius:50%;background:rgba(255,255,255,.5)}
.slider-dots span:first-child{background:var(--red)}
.hero-band{position:absolute;left:0;right:0;top:680px;height:190px;background:#141414;display:flex;align-items:center;padding:0 40px;gap:50px}
.hero-headline{font-family:"Montserrat",sans-serif;font-weight:700;font-size:27px;line-height:1.3;color:var(--white);text-transform:uppercase;width:570px;white-space:nowrap}
.hero-headline em{font-style:normal;color:var(--red);font-size:34px;display:block}
.hero-copy{color:#ccc;font-size:14.5px;line-height:1.6;width:520px}

/* upcoming */
.upcoming{top:870px;height:720px;background:var(--white)}
.upcoming .section-title{margin-top:80px}
.event-cards{position:absolute;top:180px;left:50px;right:50px;display:flex;gap:30px}
.event-card{flex:1;position:relative;background:var(--white);box-shadow:0 2px 10px rgba(0,0,0,.15);height:480px}
.event-photo{height:190px}
.event-card:nth-child(1) .event-photo{background:linear-gradient(135deg,#d94c8f,#4a7fd1 60%,#f0b23b)}
.event-card:nth-child(2) .event-photo{background:linear-gradient(135deg,#3c7fc4,#8cb4d8 55%,#2f4d6b)}
.event-card:nth-child(3) .event-photo{background:linear-gradient(135deg,#f2c05a,#d06a2a 50%,#3a5370)}
.date-badge{position:absolute;left:20px;top:-22px;width:116px;height:116px;border-radius:50%;background:var(--red);border:5px solid var(--white);color:var(--white);text-align:center;box-shadow:0 2px 6px rgba(0,0,0,.3);padding-top:16px}
.date-badge .month{font-size:13px;font-weight:600;display:block}
.date-badge .days{font-size:30px;font-weight:800;display:block;line-height:1.1}
.date-badge .year{font-size:12px;display:block}
.event-body{padding:18px 20px}
.event-tag{font-size:12px;font-weight:700;color:var(--ink);letter-spacing:1px;text-transform:uppercase}
.event-name{font-family:"Montserrat",sans-serif;font-size:31px;color:var(--red);font-weight:600;text-transform:uppercase;letter-spacing:.5px;margin:6px 0 16px;white-space:nowrap}
.event-meta{font-size:14px;line-height:1.6;color:var(--text)}
.event-card .btn{position:absolute;left:20px;right:20px;bottom:20px}

/* past */
.past{top:1590px;height:650px;background:var(--light)}
.past .section-title{margin-top:70px}
.category-select{position:absolute;right:48px;top:80px;width:270px;height:34px;background:var(--white);border:1px solid var(--line);font-size:13px;color:var(--text);padding:8px 12px;display:flex;justify-content:space-between}
.past-grid{position:absolute;top:145px;left:48px;right:48px;height:440px;display:grid;grid-template-columns:370px 260px 250px 1fr;grid-template-rows:1fr 1fr;gap:6px}
.past-item{position:relative}
.past-item.tall{grid-row:span 2}
.past-item:nth-child(1){background:linear-gradient(160deg,#3b2a1f,#8c3b22 50%,#2c2c2c)}
.past-item:nth-child(2){background:linear-gradient(160deg,#b25a3a,#d9a27a)}
.past-item:nth-child(3){background:linear-gradient(160deg,#6b5a3a,#d7c7a5)}
.past-item:nth-child(4){background:linear-gradient(160deg,#4a3a2a,#8a6a4a)}
.past-item:nth-child(5){background:linear-gradient(160deg,#1f3357,#5a3a6a)}
.past-item:nth-child(6){background:linear-gradient(160deg,#5a2a1a,#a0522d)}
.past-item:nth-child(7){background:linear-gradient(160deg,#8fae6a,#c48a6a)}
.play{position:absolute;left:50%;top:50%;width:64px;height:64px;margin:-32px 0 0 -32px;border-radius:50%;background:rgba(255,255,255,.75)}
.play::after{content:"";position:absolute;left:26px;top:20px;border-left:18px solid #444;border-top:12px solid transparent;border-bottom:12px solid transparent}

/* gallery */
.gallery{top:2240px;height:660px;background:var(--white)}
.gallery .section-title{margin-top:60px}
.gallery-intro{width:760px;margin:40px auto 0;text-align:center;font-size:14px;line-height:1.6;color:var(--text)}
.carousel{position:absolute;top:240px;left:90px;right:90px;display:flex;gap:30px}
.pavilion{flex:1;position:relative;height:245px}
.pavilion-photo{height:220px}
.pavilion:nth-child(1) .pavilion-photo{background:linear-gradient(180deg,#4a3a22,#8a7a4a 60%,#3a4a2a)}
.pavilion:nth-child(2) .pavilion-photo{background:linear-gradient(180deg,#3a2a1a,#7a6040 60%,#4a5a30)}
.pavilion:nth-child(3) .pavilion-photo{background:linear-gradient(135deg,#c44a8a,#e0c050 50%,#3a8ab0)}
.pavilion:nth-child(4) .pavilion-photo{background:linear-gradient(180deg,#5a8a4a,#a0b070 60%,#6a4a2a)}
.pavilion-label{position:absolute;left:0;right:0;bottom:0;height:42px;background:var(--red);color:var(--white);font-size:15px;font-weight:600;text-align:center;line-height:42px;border-radius:3px}
.carousel-arrow{position:absolute;top:350px;width:20px;height:40px}
.carousel-arrow.prev{left:40px}
.carousel-arrow.next{right:40px}

/* master */
.master{top:2900px;height:260px;background:var(--white)}
.master-photo{position:absolute;left:400px;right:0;top:0;bottom:0;background:linear-gradient(90deg,rgba(255,255,255,1) 0%,rgba(210,190,180,.6) 25%,#c9b3a5 45%,#9c6b5a 70%,#b84a3a 100%)}
.master-text{position:absolute;left:50px;top:50px;width:420px}
.master-title{font-family:"Montserrat",sans-serif;font-size:26px;font-weight:400;color:var(--ink);text-transform:uppercase;letter-spacing:1px;white-space:nowrap}
.master-title em{font-style:normal;color:var(--red);font-weight:700}
.master-text p{font-size:13.5px;line-height:1.6;margin-top:16px;color:var(--text)}

/* meditation */
.meditation{top:3160px;height:420px;background:var(--white)}
.meditation .section-title{margin-top:50px}
.meditation-copy{position:absolute;left:110px;right:110px;top:130px;font-size:14px;line-height:1.6;color:var(--text)}
.meditation-copy p+p{margin-top:18px}
.meditation .btn{position:absolute;left:435px;width:330px;top:300px;font-size:13px;padding:11px 0}

/* booking */
.booking{top:3580px;height:550px;background:linear-gradient(180deg,#6a6a6a 0%,#4e4e4e 60%,#2a2a2a 100%)}
.booking-figure{position:absolute;left:60px;bottom:0;width:300px;height:520px;background:linear-gradient(180deg,rgba(0,0,0,0) 0%,rgba(0,0,0,.55) 40%,rgba(0,0,0,.9) 100%)}
.booking-title{position:absolute;left:400px;right:60px;top:50px;font-family:"Montserrat",sans-serif;font-size:30px;letter-spacing:2px;color:var(--white);text-align:center;text-transform:uppercase}
.booking-title em{font-style:normal;color:var(--red);font-weight:700}
.booking .title-mark{position:absolute;left:790px;top:110px;margin:0;background:var(--white)}
.booking .title-mark::after{border-color:var(--ink)}
.booking-form{position:absolute;left:400px;width:700px;top:160px;display:grid;grid-template-columns:1fr 1fr;gap:16px 20px}
.field{height:46px;border:1px solid rgba(255,255,255,.7);border-radius:4px;color:#eee;font-size:14px;padding:13px 14px}
.field.message{grid-column:span 2;height:118px}
.booking .btn{position:absolute;left:400px;top:460px;width:200px;padding:11px 0}

/* footer */
.footer{top:4130px;height:346px;background:var(--white);text-align:center}
.footer-brand{margin-top:70px;display:flex;align-items:center;justify-content:center;gap:10px}
.footer-brand-square{width:18px;height:18px;background:var(--red)}
.footer-brand-name{font-weight:700;font-size:24px;letter-spacing:3px;color:var(--ink)}
.footer-nav{margin-top:50px;display:flex;justify-content:center;gap:22px}
.footer-nav a{font-size:13px;color:var(--muted);text-decoration:none}
.footer-nav a.active{color:var(--ink);font-weight:700}
.footer-social{margin-top:22px;display:flex;justify-content:center;gap:14px}
.footer-social span{width:20px;height:20px;border-radius:50%;background:#999}
.copyright{position:absolute;left:0;right:0;bottom:0;height:46px;line-height:46px;border-top:1px solid var(--line);font-size:12px;color:var(--ink);letter-spacing:1px}
</style>
</head>
<body>

<section class="section hero">
  <div class="hero-photo" role="img" aria-label="Open-sided jungle palapa with wooden pillars, a carved statue and garden seating"></div>
  <div class="brand"><span class="brand-square"></span><span class="brand-name">LUNEL TIKAL</span></div>
  <div class="social-top"><span></span><span></span><span></span></div>
  <nav class="main-nav">
    <a class="active">Home</a><a>News</a><a>The Project</a><a>Events</a><a>Videos</a><a>Photos</a><a>Tickets</a><a>Residential</a><a>Donate</a><a>Contact Us</a>
  </nav>
  <div class="slider-dots"><span></span><span></span><span></span></div>
  <div class="hero-band">
    <h1 class="hero-headline">We all come together from<br>all walks of life to help build <em>a paradise on earth</em></h1>
    <p class="hero-copy">The eco village project is on a 19 hectares forest land with a cenote (natural pond) as the heart centre surrounded by beautiful tropical gardens. This unique village is conceived in a mystical mayan circle as an oasis for creative arts crafts music and dance, mayan wisdom, eastern ayurveda, yoga, vipassana, meditation and silent retreat for the science of inner transformation.</p>
  </div>
</section>

<section class="section upcoming">
  <h2 class="section-title">Upcoming <em>Events</em></h2>
  <span class="title-mark"></span>
  <div class="event-cards">
    <article class="event-card">
      <div class="event-photo" role="img" aria-label="Colourful crowd at a yoga festival"></div>
      <div class="date-badge"><span class="month">NOV</span><span class="days">11-13</span><span class="year">2016</span></div>
      <div class="event-body">
        <div class="event-tag">Sunrise Circle</div>
        <div class="event-name">Yoga Festival</div>
        <div class="event-meta">@ Lunel Tikal eco-village<br>7 am to 10 pm<br>77990 Selva Alta, Mexico</div>
      </div>
      <a class="btn">Learn More</a>
    </article>
    <article class="event-card">
      <div class="event-photo" role="img" aria-label="Harbour town with boats under a blue sky"></div>
      <div class="date-badge"><span class="month">NOV</span><span class="days">18-20</span><span class="year">2016</span></div>
      <div class="event-body">
        <div class="event-tag">Open Canvas</div>
        <div class="event-name">Art Festival</div>
        <div class="event-meta">@ Lunel Tikal eco-village<br>7 am to 10 pm<br>77990 Selva Alta, Mexico</div>
      </div>
      <a class="btn">Learn More</a>
    </article>
    <article class="event-card">
      <div class="event-photo" role="img" aria-label="City bridge at golden sunset"></div>
      <div class="date-badge"><span class="month">DEC</span><span class="days">12-18</span><span class="year">2016</span></div>
      <div class="event-body">
        <div class="event-tag">Healing Hands</div>
        <div class="event-name">Thai Massage</div>
        <div class="event-meta">@ Lunel Tikal eco-village<br>2 am to 6 pm<br>77990 Selva Alta, Mexico</div>
      </div>
      <a class="btn">Learn More</a>
    </article>
  </div>
</section>

<section class="section past">
  <h2 class="section-title">Past <em>Events</em></h2>
  <span class="title-mark"></span>
  <div class="category-select"><span>Browse Events By Category</span><span>&#9662;</span></div>
  <div class="past-grid">
    <div class="past-item tall" role="img" aria-label="Dancers in feathered ceremonial costume"><span class="play"></span></div>
    <div class="past-item" role="img" aria-label="Performer in red robes on stage"></div>
    <div class="past-item" role="img" aria-label="Outdoor gathering in a garden"></div>
    <div class="past-item" role="img" aria-label="Musicians at an evening ceremony"><span class="play"></span></div>
    <div class="past-item" role="img" aria-label="Dancers under blue night lights"></div>
    <div class="past-item" role="img" aria-label="Drummer in traditional headdress"><span class="play"></span></div>
    <div class="past-item" role="img" aria-label="Group of festival guests posing together"></div>
  </div>
</section>

<section class="section gallery">
  <h2 class="section-title">Eco Village <em>Gallery</em></h2>
  <span class="title-mark"></span>
  <p class="gallery-intro">The eco village project is on a 19 hectares forest land with a cenote (natural pond) as the heart centre surrounded by beautiful tropical gardens. Please click on each gallery below to view larger images.</p>
  <svg class="carousel-arrow prev" viewBox="0 0 20 40"><polyline points="16,4 4,20 16,36" fill="none" stroke="#bbb" stroke-width="3"/></svg>
  <div class="carousel">
    <div class="pavilion"><div class="pavilion-photo" role="img" aria-label="Thatched pavilion among trees"></div><div class="pavilion-label">Fern Pavilion</div></div>
    <div class="pavilion"><div class="pavilion-photo" role="img" aria-label="Open wooden pavilion interior"></div><div class="pavilion-label">Reed Pavilion</div></div>
    <div class="pavilion"><div class="pavilion-photo" role="img" aria-label="Colourful mural at the welcome center"></div><div class="pavilion-label">Welcome Center</div></div>
    <div class="pavilion"><div class="pavilion-photo" role="img" aria-label="Residential studio in the garden"></div><div class="pavilion-label">Cenote Studio - Residential</div></div>
  </div>
  <svg class="carousel-arrow next" viewBox="0 0 20 40"><polyline points="4,4 16,20 4,36" fill="none" stroke="#bbb" stroke-width="3"/></svg>
</section>

<section class="section master">
  <div class="master-photo" role="img" aria-label="The master in white robes leading a group meditation"></div>
  <div class="master-text">
    <h2 class="master-title">Message from <em>The Master</em></h2>
    <p>Welcome to our village in the jungle, a space of silence and love. Here we meet nature, meditation and one another without masks. Come as you are, rest in the heart, and let the forest teach you stillness. Every seeker is a guest in this home, and every guest becomes family.</p>
  </div>
</section>

<section class="section meditation">
  <h2 class="section-title">Meditation &amp; <em>Yoga</em></h2>
  <span class="title-mark"></span>
  <div class="meditation-copy">
    <p>Our inner science school offers daily sessions of yoga, pranayama and vipassana in open pavilions beside the cenote. Mornings begin with silent sitting and gentle breath work, followed by asana practice guided by resident teachers, and evenings close with dance and music under the stars.</p>
    <p>Therapies such as mystic rose, no mind, prana healing and work as meditation are offered freely to all guests. We accept donations out of gratitude, so that everyone may taste the silence within.</p>
  </div>
  <a class="btn">More About Meditation &amp; Yoga</a>
</section>

<section class="section booking">
  <div class="booking-figure" role="img" aria-label="Silhouette of a person in a standing yoga pose at dusk"></div>
  <h2 class="booking-title">Residential <em>Booking</em></h2>
  <span class="title-mark"></span>
  <div class="booking-form">
    <div class="field">Name</div>
    <div class="field">Email Address</div>
    <div class="field">Desired Check-in Date</div>
    <div class="field">Desired Check-out Date</div>
    <div class="field message">Message</div>
  </div>
  <a class="btn">Submit</a>
</section>

<footer class="section footer">
  <div class="footer-brand"><span class="footer-brand-square"></span><span class="footer-brand-name">LUNEL TIKAL</span></div>
  <nav class="footer-nav">
    <a class="active">Home</a><a>News</a><a>The Project</a><a>Events</a><a>Videos</a><a>Photos</a><a>Tickets</a><a>Residential</a><a>Donate</a><a>Contact</a>
  </nav>
  <div class="footer-social"><span></span><span></span><span></span><span></span></div>
  <div class="copyright">COPYRIGHT © 2016 LUNEL TIKAL. ALL RIGHTS RESERVED.</div>
</footer>

</body>
</html>
```